【 概要 】 弊社の採用募集用のバナー制作をお願いいたします。 大々的に広告を打つので、複数で採用で検討しております。 また、弊社には現在、似たような案件が多いため、『キーワードだけ変えていただき採用』なども検討しており、目安は10名近い採用を考えておりますので奮ってご応募くださいませ。 年内で急ぎたいため、早期終了も検討しておりますのでお早めにどうぞ! 【 依頼内容 】 ・サイズ: 横1200 × 縦1200px ・作成数: 2種類(採用確定した方だけ、全く同じデザインで縦長へ配置換えをしたリサイズもお願いいたします) ・利用用途:リスティング広告、ウェブサイトなど ・キーワード:テキストファイルに添付 ・納品:ご提案はPNG。自社で微調整のために、採用された方のみ編集できるようPSDデータも納品お願いいたします。 【 デザインイメージ 】 ・ターゲット層:20〜40代の女性 ・雰囲気:構成などは全てお任せ 【 契約金額(税抜) 】 15000円 ※契約金額(税込)からシステム利用料を差し引いた金額が、ワーカーさまの受取金額となります その他ご質問等ありましたら、気軽にお問い合わせください。 ご応募をお待ちしております! |
とてもカラフルでインパクトが強い作品で理想と感じました。
たくさんのご応募ありがとうございました。
まずは1位採用で確定させていただきましたが、今回は複数採用でぜひ他にも気になる素敵な作品がございますので、別途またご連絡させていただきます方はご対応よろしくお願いいたします。

```html
<!DOCTYPE html>
<html lang="ja">
<head>
<meta charset="utf-8">
<title>自宅でカンタンお仕事 求人バナー</title>
<link rel="stylesheet" href="https://fonts.googleapis.com/css2?family=M+PLUS+Rounded+1c:wght@800;900&display=swap">
<style>
  :root {
    --teal: #17b3a6;
    --teal-dark: #0f9d92;
    --teal-light: #5fd0c4;
    --orange: #f39a2e;
    --white: #ffffff;
    --bg-light: #f4f8f6;
    --bg-green: #dcebe2;
    --photo-skin: #e8cdb5;
    --photo-knit: #f1e6d8;
    --photo-hair: #7a5a44;
  }
  * { margin: 0; padding: 0; box-sizing: border-box; }
  html, body { width: 1200px; height: 1200px; overflow: hidden; background: var(--white); }
  .banner {
    position: relative;
    width: 1200px;
    height: 1200px;
    background: var(--teal);
    font-family: "M PLUS Rounded 1c", sans-serif;
    overflow: hidden;
  }
  .stage {
    position: absolute;
    left: 32px; top: 32px; right: 32px; bottom: 32px;
    background: linear-gradient(100deg, var(--white) 0%, var(--bg-light) 40%, var(--bg-green) 100%);
    overflow: hidden;
  }
  .photo {
    position: absolute;
    left: 540px; top: 40px; width: 596px; height: 930px;
    border-radius: 48% 48% 0 0 / 30% 30% 0 0;
    background:
      radial-gradient(ellipse 34% 22% at 52% 26%, var(--photo-skin) 0%, rgba(232,205,181,0.9) 55%, rgba(232,205,181,0) 100%),
      radial-gradient(ellipse 44% 32% at 55% 24%, rgba(122,90,68,0.55) 0%, rgba(122,90,68,0.25) 60%, rgba(122,90,68,0) 100%),
      radial-gradient(ellipse 60% 50% at 52% 78%, var(--photo-knit) 0%, rgba(241,230,216,0.85) 60%, rgba(241,230,216,0) 100%);
  }
  .headline { position: absolute; color: var(--teal); font-weight: 900; white-space: nowrap; }
  .outlined {
    -webkit-text-stroke: 18px var(--white);
    paint-order: stroke fill;
    text-shadow: 0 4px 10px rgba(0,0,0,0.12);
  }
  .headline-home { left: 155px; top: 70px; font-size: 140px; line-height: 1; }
  .headline-home .small { font-size: 100px; }
  .easy { position: absolute; left: 115px; top: 235px; display: flex; align-items: flex-start; }
  .easy-chip {
    width: 146px; height: 146px; border-radius: 50%;
    background: var(--teal);
    border: 9px solid var(--white);
    box-shadow: 0 4px 10px rgba(0,0,0,0.12);
    color: var(--white);
    font-size: 92px; font-weight: 900; line-height: 1;
    display: flex; align-items: center; justify-content: center;
    margin-right: -12px;
  }
  .easy-chip.small { width: 108px; height: 108px; font-size: 64px; margin-top: 42px; }
  .headline-work { left: 110px; top: 395px; font-size: 170px; line-height: 1; letter-spacing: -6px; }
  .badge {
    position: absolute;
    width: 216px; height: 216px; border-radius: 50%;
    background: var(--orange);
    border: 8px solid var(--white);
    color: var(--white);
    font-size: 32px; font-weight: 900; line-height: 1.35;
    display: flex; align-items: center; justify-content: center; text-align: center;
    box-shadow: 0 4px 10px rgba(0,0,0,0.12);
    white-space: nowrap;
  }
  .badge-interview { left: 112px; top: 680px; }
  .badge-monitor { left: 334px; top: 652px; }
  .pay-band {
    position: absolute;
    left: 0; right: 0; bottom: 0; height: 170px;
    background: linear-gradient(90deg, var(--teal-dark) 0%, var(--teal) 55%, var(--teal-light) 100%);
    color: var(--white);
    display: flex; align-items: baseline;
    padding: 28px 0 0 46px;
    font-weight: 900;
    white-space: nowrap;
  }
  .pay-unit { font-size: 64px; margin-right: 40px; }
  .pay-amount { font-size: 128px; letter-spacing: 2px; line-height: 1; }
  .pay-yen { font-size: 66px; margin-left: 12px; }
  .pay-tilde { font-size: 66px; margin-left: 18px; }
</style>
</head>
<body>
  <div class="banner">
    <div class="stage">
      <div class="photo" role="img" aria-label="スマートフォンを手に笑顔で過ごす女性の写真"></div>

      <div class="headline headline-home outlined">自宅<span class="small">で</span></div>

      <div class="easy" aria-label="カンタン">
        <span class="easy-chip">カ</span>
        <span class="easy-chip small">ン</span>
        <span class="easy-chip">タ</span>
        <span class="easy-chip small">ン</span>
      </div>

      <div class="headline headline-work outlined">お仕事！</div>

      <div class="badge badge-interview">面接不要で<br>全国対応!</div>
      <div class="badge badge-monitor">短期アプリ<br>モニター<br>募集!</div>

      <div class="pay-band">
        <span class="pay-unit">1時間</span>
        <span class="pay-amount">2500</span>
        <span class="pay-yen">円</span>
        <span class="pay-tilde">～</span>
      </div>
    </div>
  </div>
</body>
</html>
```